Photographer Card

I'm currently doing freelance photography and i need a creative design name card especially when i attend events.
I require a design that makes a STATEMENT.
Simple, elegant and nothing like the usual name cards ive seen around (Example: with a camera/tripod etc in the design).

Photographer: Dorian VP
Mobile: +65 84126957
E-mail: Dorian.VP.Photography@mailvista.net
FriendLane: www.friendlane.net/dorian.vp.photography

Thanks for your time and hope it will turn out well! :)
Updates

Thanks for all your inputs!

Im liking the cursive feel.

Id prefer not to include the title "freelance"  :)

Also, im looking for a logo to establish myself

http://www.artmosaic.net/art/Cotton-Business-Card-583021746

Hi all! Thanks for the designs

"Capturing magical moments"
"Capturing magical moments that are gone forever"

Back design can be in big font "look HERE"

Maybe with focusing box 

Names can be played with horizontal and vertical.

Industry/Entity Type

Camera

Font styles to use
Script

```html
<!DOCTYPE html>
<html lang="en">
<head>
<meta charset="utf-8">
<title>Dorian VP Photography – Business Card</title>
<link rel="stylesheet" href="https://fonts.googleapis.com/css2?family=Michroma&family=Cormorant+Garamond:ital,wght@1,700&display=swap">
<style>
  :root {
    --paper-light: #ece6d8;
    --paper-mid: #d9d0bd;
    --paper-edge: #9e937e;
    --name-red: #7a1414;
    --ink: #151515;
    --shade-dark: #2e2e30;
    --shade-mid: #6a6a6e;
  }
  html, body {
    margin: 0;
    padding: 0;
    width: 1200px;
    height: 682px;
    overflow: hidden;
    background: #ffffff;
  }
  .card {
    position: relative;
    width: 1200px;
    height: 682px;
    overflow: hidden;
    background:
      radial-gradient(ellipse 75% 70% at 55% 42%, var(--paper-light) 0%, var(--paper-mid) 60%, var(--paper-edge) 100%);
  }
  .brand-name {
    position: absolute;
    left: 62px;
    top: 132px;
    margin: 0;
    font-family: "Michroma", sans-serif;
    font-weight: 400;
    font-size: 62px;
    line-height: 1;
    letter-spacing: 10px;
    color: var(--name-red);
    text-transform: uppercase;
  }
  .brand-trade {
    position: absolute;
    left: 372px;
    top: 246px;
    margin: 0;
    font-family: "Michroma", sans-serif;
    font-size: 34px;
    line-height: 1;
    letter-spacing: 26px;
    color: var(--ink);
    text-transform: uppercase;
  }
  .feature-image {
    position: absolute;
    left: 90px;
    top: 330px;
    width: 390px;
    height: 310px;
    border-radius: 50%;
    background: radial-gradient(ellipse at 55% 55%, var(--shade-mid) 0%, var(--shade-dark) 45%, rgba(46,46,48,0.6) 65%, rgba(46,46,48,0) 72%);
  }
  .contact-list {
    position: absolute;
    left: 482px;
    top: 470px;
    margin: 0;
    padding: 0;
    list-style: none;
  }
  .contact-item {
    display: flex;
    align-items: center;
    height: 75px;
  }
  .contact-icon {
    width: 42px;
    height: 42px;
    margin-right: 20px;
    flex: none;
  }
  .contact-text {
    font-family: "Cormorant Garamond", serif;
    font-style: italic;
    font-weight: 700;
    font-variant: small-caps;
    font-size: 30px;
    color: var(--ink);
    letter-spacing: 0.5px;
    white-space: nowrap;
  }
  .contact-text.phone { font-size: 26px; }
</style>
</head>
<body>
  <main class="card">
    <h1 class="brand-name">Dorian VP</h1>
    <p class="brand-trade">Photography</p>

    <div class="feature-image" role="img" aria-label="Dark grey photographic image area"></div>

    <ul class="contact-list">
      <li class="contact-item">
        <svg class="contact-icon" viewBox="0 0 42 42" aria-hidden="true">
          <rect x="6" y="18" width="30" height="18" rx="3" fill="var(--ink)"/>
          <path d="M4 16 Q21 4 38 16 L34 20 Q21 12 8 20 Z" fill="var(--ink)"/>
          <g fill="var(--paper-light)">
            <circle cx="14" cy="24" r="1.6"/><circle cx="21" cy="24" r="1.6"/><circle cx="28" cy="24" r="1.6"/>
            <circle cx="14" cy="30" r="1.6"/><circle cx="21" cy="30" r="1.6"/><circle cx="28" cy="30" r="1.6"/>
          </g>
        </svg>
        <span class="contact-text phone">+65 84126957</span>
      </li>
      <li class="contact-item">
        <svg class="contact-icon" viewBox="0 0 42 42" aria-hidden="true">
          <rect x="4" y="10" width="34" height="22" fill="var(--ink)"/>
          <path d="M5 11 L21 24 L37 11" fill="none" stroke="var(--paper-light)" stroke-width="2"/>
        </svg>
        <span class="contact-text">Dorian.VP.Photography@mailvista.net</span>
      </li>
      <li class="contact-item">
        <svg class="contact-icon" viewBox="0 0 42 42" aria-hidden="true">
          <circle cx="21" cy="21" r="13" fill="var(--name-red)"/>
        </svg>
        <span class="contact-text">www.friendlane.net/dorian.vp.photography</span>
      </li>
    </ul>
  </main>
</body>
</html>
```